Design of two graphics from basic existing design & colours

I have two graphics which I currently use but they are nothing special. We would like to transform these two graphics, using our existing logo colour, into something special. The outputs will be used:

- on our website;
- in a powerpoint sales presentation;
- in email campaigns; and
- to print for handing to prospects at the end of a sales presentation.

Please just submit one of the graphics and if we like the design, we will ask you to work on the second graphic. These two graphics are critical to our marketing and will be used together so we need them to have a similar look and feel.

```html
<!DOCTYPE html>
<html lang="en">
<head>
<meta charset="utf-8">
<title>Performance Cycle Revision</title>
<link href="https://fonts.googleapis.com/css2?family=Arimo:wght@400;700&display=swap" rel="stylesheet">
<style>
  :root {
    --red: #c9443a;
    --black: #1e1e1e;
    --charcoal: #3a3a3c;
    --grey: #9e9e9e;
    --maroon: #5e2a20;
    --title: #6b2a1e;
    --ink: #1a1a1a;
    --white: #ffffff;
  }
  html, body {
    margin: 0;
    padding: 0;
    overflow: hidden;
    background: var(--white);
  }
  .slide {
    position: relative;
    width: 1200px;
    height: 675px;
    overflow: hidden;
    background: var(--white);
    font-family: "Arimo", Arial, sans-serif;
  }
  .slide-title {
    position: absolute;
    left: 163px;
    top: 258px;
    margin: 0;
    font-size: 32px;
    line-height: 40px;
    font-weight: 700;
    color: var(--title);
  }
  .brand {
    position: absolute;
    left: 50px;
    top: 606px;
    display: flex;
    align-items: center;
    gap: 8px;
  }
  .brand-mark {
    width: 14px;
    height: 14px;
    background: var(--red);
    flex: none;
  }
  .brand-name {
    font-size: 16px;
    line-height: 19px;
    font-weight: 700;
    color: var(--red);
    letter-spacing: 0.5px;
  }
  .artwork {
    position: absolute;
    inset: 0;
  }
  .seg-red { fill: var(--red); }
  .seg-black { fill: var(--black); }
  .seg-charcoal { fill: var(--charcoal); }
  .seg-grey { fill: var(--grey); }
  .seg-label {
    fill: var(--white);
    font-family: "Arimo", Arial, sans-serif;
    font-weight: 700;
    font-size: 13px;
    text-anchor: middle;
  }
  .axis-caption {
    fill: var(--ink);
    font-family: "Arimo", Arial, sans-serif;
    font-weight: 700;
    font-size: 13px;
    text-anchor: middle;
  }
  .hub-box { fill: var(--maroon); }
  .hub-label {
    fill: var(--white);
    font-family: "Arimo", Arial, sans-serif;
    font-weight: 700;
    font-size: 16px;
    text-anchor: middle;
  }
  .divider {
    stroke: var(--ink);
    stroke-width: 3;
    stroke-dasharray: 2 5;
    stroke-linecap: round;
  }
  .band-maroon { fill: var(--maroon); }
  .band-red { fill: var(--red); }
  .band-black { fill: var(--black); }
</style>
</head>
<body>
<main class="slide">
  <h1 class="slide-title">Performance<br>Cycle Revision</h1>

  <svg class="artwork" width="1200" height="675" viewBox="0 0 1200 675" aria-label="Performance cycle diagram">
    <defs>
      <path id="petal" d="M -69.6 -259.8 A 269 269 0 0 1 69.6 -259.8 C 62 -180 30 -122 0 -122 C -30 -122 -62 -180 -69.6 -259.8 Z"/>
      <g id="flow-arrow"><rect x="-8" y="-2" width="11" height="4"/><polygon points="2,-6 10,0 2,6"/></g>
    </defs>

    <polygon class="band-maroon" points="219,675 262,609 700,609 670,675"/>
    <polygon class="band-red" points="650,675 690,609 968,609 928,675"/>
    <polygon class="band-black" points="926,675 966,609 1200,609 1200,675"/>

    <g class="cycle" transform="translate(801 300)">
      <use href="#petal" class="seg-red" transform="rotate(0)"/>
      <use href="#petal" class="seg-black" transform="rotate(36)"/>
      <use href="#petal" class="seg-grey" transform="rotate(72)"/>
      <use href="#petal" class="seg-red" transform="rotate(108)"/>
      <use href="#petal" class="seg-charcoal" transform="rotate(144)"/>
      <use href="#petal" class="seg-red" transform="rotate(180)"/>
      <use href="#petal" class="seg-black" transform="rotate(216)"/>
      <use href="#petal" class="seg-grey" transform="rotate(252)"/>
      <use href="#petal" class="seg-red" transform="rotate(288)"/>
      <use href="#petal" class="seg-charcoal" transform="rotate(324)"/>

      <use href="#flow-arrow" class="seg-red" transform="rotate(18) translate(0 -180)"/>
      <use href="#flow-arrow" class="seg-black" transform="rotate(54) translate(0 -180)"/>
      <use href="#flow-arrow" class="seg-grey" transform="rotate(90) translate(0 -180)"/>
      <use href="#flow-arrow" class="seg-red" transform="rotate(126) translate(0 -180)"/>
      <use href="#flow-arrow" class="seg-charcoal" transform="rotate(162) translate(0 -180)"/>
      <use href="#flow-arrow" class="seg-red" transform="rotate(198) translate(0 -180)"/>
      <use href="#flow-arrow" class="seg-black" transform="rotate(234) translate(0 -180)"/>
      <use href="#flow-arrow" class="seg-grey" transform="rotate(270) translate(0 -180)"/>
      <use href="#flow-arrow" class="seg-red" transform="rotate(306) translate(0 -180)"/>
      <use href="#flow-arrow" class="seg-charcoal" transform="rotate(342) translate(0 -180)"/>

      <text class="seg-label" x="0" y="-214"><tspan x="0" dy="0">Strategic</tspan><tspan x="0" dy="16">Plan</tspan></text>
      <text class="seg-label" x="123" y="-180"><tspan x="123" dy="0">Annual</tspan><tspan x="123" dy="16">business</tspan><tspan x="123" dy="16">plan</tspan></text>
      <text class="seg-label" x="188" y="-70"><tspan x="188" dy="0">Departamental</tspan><tspan x="188" dy="16">plans</tspan></text>
      <text class="seg-label" x="188" y="36"><tspan x="188" dy="0">Annual</tspan><tspan x="188" dy="16">performance</tspan><tspan x="188" dy="16">objectives &amp;</tspan><tspan x="188" dy="16">KPIs</tspan></text>
      <text class="seg-label" x="118" y="150"><tspan x="118" dy="0">Monthly</tspan><tspan x="118" dy="16">performance</tspan><tspan x="118" dy="16">meetings</tspan></text>
      <text class="seg-label" x="0" y="190"><tspan x="0" dy="0">Individual</tspan><tspan x="0" dy="16">performance</tspan><tspan x="0" dy="16">plan</tspan></text>
      <text class="seg-label" x="-120" y="144"><tspan x="-120" dy="0">Individual</tspan><tspan x="-120" dy="16">development</tspan><tspan x="-120" dy="16">plan</tspan></text>
      <text class="seg-label" x="-185" y="50"><tspan x="-185" dy="0">Succession</tspan><tspan x="-185" dy="16">plan</tspan></text>
      <text class="seg-label" x="-185" y="-70"><tspan x="-185" dy="0">Business</tspan><tspan x="-185" dy="16">reviews</tspan></text>
      <text class="seg-label" x="-123" y="-186"><tspan x="-123" dy="0">Advisory</tspan><tspan x="-123" dy="16">board</tspan><tspan x="-123" dy="16">meetings</tspan></text>

      <line class="divider" x1="-268" y1="0" x2="-84" y2="0"/>
      <line class="divider" x1="84" y1="0" x2="256" y2="0"/>
      <text class="axis-caption" x="0" y="-45">Managing structure</text>
      <text class="axis-caption" x="0" y="51">Managing performance</text>
      <rect class="hub-box" x="-72" y="-16" width="144" height="32" rx="6"/>
      <text class="hub-label" x="0" y="6">Advisory Board</text>
    </g>
  </svg>

  <div class="brand">
    <span class="brand-mark"></span>
    <span class="brand-name">CRESTLINE<br>LEADERSHIP</span>
  </div>
</main>
</body>
</html>
```